Copperleaf Motorized Shade Business Card

Hello, we've had our logo made. Now we are looking for a clean and cool looking business card. One side can just be the logo with any design elements that might look good with it. The other side will be Name, Phone Number and Email. There will not be an address on the card.

```html
<!DOCTYPE html>
<html lang="en">
<head>
<meta charset="utf-8">
<title>Copperleaf Motorized Shade – Business Card</title>
<link rel="stylesheet" href="https://fonts.googleapis.com/css2?family=Open+Sans:wght@400;600;700&display=swap">
<style>
  :root {
    --backdrop: #9b9b9b;
    --navy: #1f3c6f;
    --sky: #29a8e0;
    --white: #ffffff;
    --ink-soft: #555a60;
  }
  * { margin: 0; padding: 0; box-sizing: border-box; }
  html, body {
    width: 1021px;
    height: 1200px;
    overflow: hidden;
    background: var(--backdrop);
    font-family: "Open Sans", Arial, sans-serif;
  }
  .card {
    position: absolute;
    left: 138px;
    width: 745px;
    height: 425px;
  }
  .card--front {
    top: 121px;
    background: var(--navy);
  }
  .card--back {
    top: 652px;
    background: var(--white);
  }

  /* Brand name lockup */
  .brand {
    position: absolute;
    display: flex;
    align-items: center;
    gap: 16px;
    font-weight: 600;
    line-height: 1;
  }
  .brand__mark {
    flex: none;
    background: var(--sky);
  }
  .brand__text { display: flex; flex-direction: column; }
  .brand__name { letter-spacing: 1px; }
  .brand__tagline { letter-spacing: 0.42em; }

  .card--front .brand {
    left: 50%;
    top: 50%;
    transform: translate(-50%, -50%);
    color: var(--white);
  }
  .card--front .brand__mark { width: 26px; height: 26px; }
  .card--front .brand__name { font-size: 64px; }
  .card--front .brand__tagline { font-size: 18px; margin-top: 14px; }

  .card--back .brand {
    right: 40px;
    bottom: 50px;
    color: var(--navy);
    gap: 12px;
  }
  .card--back .brand__mark { width: 16px; height: 16px; }
  .card--back .brand__name { font-size: 38px; }
  .card--back .brand__tagline { font-size: 11px; margin-top: 9px; }

  /* Contact block */
  .contact {
    position: absolute;
    left: 38px;
    top: 44px;
  }
  .contact__name {
    font-size: 28px;
    font-weight: 700;
    color: var(--navy);
    letter-spacing: 0.2px;
    line-height: 1.1;
  }
  .contact__role {
    font-size: 20px;
    color: var(--ink-soft);
    margin-top: 4px;
  }
  .contact__list {
    list-style: none;
    margin-top: 30px;
  }
  .contact__item {
    display: flex;
    align-items: center;
    gap: 6px;
    font-size: 20px;
    color: var(--ink-soft);
    height: 28px;
  }
  .contact__icon { width: 18px; height: 18px; flex: none; }
</style>
</head>
<body>

<section class="card card--front" aria-label="Card front">
  <div class="brand">
    <span class="brand__mark"></span>
    <div class="brand__text">
      <span class="brand__name">COPPERLEAF</span>
      <span class="brand__tagline">MOTORIZED SHADE</span>
    </div>
  </div>
</section>

<section class="card card--back" aria-label="Card back">
  <div class="contact">
    <h1 class="contact__name">DANA WHITLOCK</h1>
    <p class="contact__role">President</p>
    <ul class="contact__list">
      <li class="contact__item">
        <svg class="contact__icon" viewBox="0 0 24 24" aria-hidden="true">
          <path fill="#29a8e0" d="M6.6 10.8a15.1 15.1 0 0 0 6.6 6.6l2.2-2.2c.3-.3.7-.4 1-.2 1.1.4 2.3.6 3.6.6.6 0 1 .4 1 1V20c0 .6-.4 1-1 1A17 17 0 0 1 3 4c0-.6.4-1 1-1h3.5c.6 0 1 .4 1 1 0 1.3.2 2.5.6 3.6.1.3 0 .7-.2 1z"/>
        </svg>
        555-310-4827
      </li>
      <li class="contact__item">
        <svg class="contact__icon" viewBox="0 0 24 24" aria-hidden="true">
          <path fill="#29a8e0" d="M3 6h18v12H3z"/>
          <path fill="none" stroke="#fff" stroke-width="1.6" d="M3.5 6.8 12 13l8.5-6.2"/>
        </svg>
        danawhitlock@mail.com
      </li>
      <li class="contact__item">
        <svg class="contact__icon" viewBox="0 0 24 24" aria-hidden="true">
          <circle cx="12" cy="12" r="9" fill="#29a8e0"/>
          <path fill="none" stroke="#fff" stroke-width="1.3" d="M3 12h18M12 3c3 3 3 15 0 18M12 3c-3 3-3 15 0 18"/>
        </svg>
        www.copperleafshades.com
      </li>
    </ul>
  </div>

  <div class="brand">
    <span class="brand__mark"></span>
    <div class="brand__text">
      <span class="brand__name">COPPERLEAF</span>
      <span class="brand__tagline">MOTORIZED SHADE</span>
    </div>
  </div>
</section>

</body>
</html>
```